Podcast cover art (not a logo)

I’m launching an audio-only podcast for parents of neurodivergent children. The podcast is meant to feel like a calm, trusted professional voice — not a brand or a performance.

Style direction:
--Clean and minimal
--Calm and grounded
--Professional, not playful
--Nothing flashy, loud, or busy
--No cartoon imagery

Content on the cover:
--Podcast title: Under the Quiet Surface
--Subtitle or tagline: Calm Guidance for Parents of Neurodivergent Children (or Understanding Neurodivergent Kids)
--No episode numbers, no dates

Design preferences:
--Text-forward design
--Neutral or soft colors (muted blues, grays, off-whites)
--High contrast for readability at small sizes
--Simple, timeless font

What I do NOT want:
--A logo or branding system
--Illustrations of children or families
--Bright colors or playful graphics
--Trendy fonts or visual effects

Technical requirements:
--Square image
--3000 × 3000 pixels
--RGB color mode
--JPEG or PNG
--File size under 500 KB

Deliverables:
--Final cover art file
--Optional: one or two alternate background color versions

```html
<!DOCTYPE html>
<html lang="en">
<head>
<meta charset="utf-8">
<title>Under the Quiet Surface — Podcast Cover</title>
<link rel="stylesheet" href="https://fonts.googleapis.com/css2?family=Gilda+Display&family=Poppins:wght@300;400&display=swap">
<style>
  :root {
    --page-bg: #f5f6f7;
    --sky-center: #f4f9fb;
    --sky-mid: #cfe6ee;
    --sky-edge: #8fc1d4;
    --deep-blue: #3b7caa;
    --title-blue: #3a79a6;
    --halo: #ffffff;
    --subtitle: #ffffff;
  }
  * { margin: 0; padding: 0; box-sizing: border-box; }
  html, body {
    width: 1200px;
    height: 590px;
    overflow: hidden;
    background: var(--page-bg);
  }
  .stage {
    position: relative;
    width: 1200px;
    height: 590px;
  }
  .cover {
    position: absolute;
    left: 320px;
    top: 15px;
    width: 560px;
    height: 560px;
    overflow: hidden;
  }
  .cover-art {
    position: absolute;
    inset: 0;
    width: 560px;
    height: 560px;
    display: block;
  }
  .title {
    position: absolute;
    left: 0;
    right: 0;
    top: 46px;
    text-align: center;
    font-family: "Gilda Display", "Times New Roman", serif;
    color: var(--title-blue);
    font-weight: 400;
  }
  .title-line { display: block; }
  .title-line--major {
    font-size: 96px;
    line-height: 84px;
    letter-spacing: -1px;
  }
  .title-line--minor {
    font-size: 56px;
    line-height: 52px;
  }
  .tagline {
    position: absolute;
    left: 0;
    right: 0;
    top: 437px;
    text-align: center;
    font-family: "Poppins", Arial, sans-serif;
    font-weight: 300;
    font-size: 21px;
    line-height: 26px;
    letter-spacing: 1.2px;
    color: var(--subtitle);
  }
  .tagline span { display: block; }
</style>
</head>
<body>
<main class="stage">
  <section class="cover" aria-label="Podcast cover: Under the Quiet Surface">
    <svg class="cover-art" viewBox="0 0 560 560" aria-hidden="true">
      <defs>
        <radialGradient id="sky" cx="0.5" cy="0.46" r="0.72">
          <stop offset="0" stop-color="var(--sky-center)"/>
          <stop offset="0.45" stop-color="var(--sky-mid)"/>
          <stop offset="1" stop-color="var(--sky-edge)"/>
        </radialGradient>
        <linearGradient id="halo-fade" x1="0" y1="0" x2="0" y2="1">
          <stop offset="0" stop-color="var(--halo)" stop-opacity="0.55"/>
          <stop offset="0.35" stop-color="var(--halo)" stop-opacity="1"/>
        </linearGradient>
      </defs>
      <rect class="sky" width="560" height="560" fill="url(#sky)"/>
      <ellipse class="halo" cx="280" cy="640" rx="342" ry="302" fill="url(#halo-fade)"/>
      <circle class="horizon" cx="280" cy="629" r="288" fill="var(--deep-blue)"/>
    </svg>
    <h1 class="title">
      <span class="title-line title-line--major">Under</span>
      <span class="title-line title-line--minor">the Quiet</span>
      <span class="title-line title-line--major">Surface</span>
    </h1>
    <p class="tagline">
      <span>Calm Guidance for Parents of</span>
      <span>Neurodivergent Children</span>
    </p>
  </section>
</main>
</body>
</html>
```